Etikett-Design für Olivenöl
Unsere Vorgaben wurden gut aufgenommen. Der erste Entwurf hat uns sofort angesprochen. Wir hatten noch ein paar Modifikationen und das Projekt war sehr schnell erfolgreich abgeschlossen. Wir werden weitere Themen hier beauftragen. Besten Dank.
Zielgruppe
Einzelhandel. Die Zielgruppe ist 30 bis 55 Jahre alt, weiblich sowie männlich.
Aufgabenstellung
Das Label für die 100ml große Flasche soll 13,4 cm x 6,7 cm groß sein.
In der Flasche ist ein hochwertiges natives Olivenöl.
Das Design soll frisch, klar, ansprechend, anziehend und freundlich sein.

```html
<!DOCTYPE html>
<html lang="de">
<head>
<meta charset="utf-8">
<title>Serevo Olivenöl – Etikett</title>
<link href="https://fonts.googleapis.com/css2?family=Fira+Sans+Condensed:wght@300;400;600&family=Montserrat:wght@400;500;600;700&family=Oranienbaum&display=swap" rel="stylesheet">
<style>
  :root {
    --page: #f2ede2;
    --cream: #f5f5ec;
    --olive: #b6bb57;
    --ink: #3b3b3b;
    --white: #ffffff;
    --heart: #ef8a87;
    --leaf: #d3d7cd;
  }
  * { margin: 0; padding: 0; box-sizing: border-box; }
  html, body { width: 1123px; height: 1200px; overflow: hidden; background: var(--page); }
  .label {
    position: absolute; left: 30px; top: 326px;
    width: 1063px; height: 548px;
    background: var(--cream); overflow: hidden;
    font-family: "Fira Sans Condensed", sans-serif; color: var(--ink);
  }
  .abs { position: absolute; }
  .leaf-decor { position: absolute; border-radius: 50%; }
  .leaf-decor--left {
    left: -30px; top: -20px; width: 230px; height: 230px;
    background: radial-gradient(circle at 45% 45%, rgba(211,215,205,.85), rgba(211,215,205,.35) 55%, rgba(245,245,236,0) 72%);
  }
  .leaf-decor--right {
    left: 770px; top: 180px; width: 270px; height: 150px;
    background: radial-gradient(ellipse at 50% 55%, rgba(211,215,205,.85), rgba(211,215,205,.35) 55%, rgba(245,245,236,0) 72%);
  }
  .facts { left: 38px; top: 30px; font-weight: 300; font-size: 19px; line-height: 22px; }
  .donation { left: 38px; top: 240px; width: 160px; font-family: "Montserrat", sans-serif; font-weight: 500; font-size: 16px; line-height: 23px; }
  .donation__heart { position: absolute; left: 40px; top: -4px; width: 56px; height: 56px; }
  .donation__text { position: relative; }
  .donation__text span { padding-left: 20px; }
  .est { left: 381px; width: 300px; top: 32px; text-align: center; font-family: "Montserrat", sans-serif; font-size: 16px; }
  .brand { left: 381px; width: 300px; top: 120px; display: flex; justify-content: center; align-items: center; gap: 14px; }
  .brand__dot { width: 16px; height: 16px; border-radius: 50%; background: var(--olive); }
  .brand__name { font-family: "Oranienbaum", serif; font-size: 60px; letter-spacing: 2px; color: var(--ink); }
  .tagline { left: 331px; width: 400px; top: 252px; text-align: center; font-family: "Montserrat", sans-serif; font-weight: 600; font-size: 27px; }
  .bottler { left: 800px; width: 240px; top: 44px; text-align: center; font-weight: 300; font-size: 17.5px; line-height: 21.5px; }
  .bottler__mail { margin-top: 21px; }

  .band { position: absolute; left: 0; top: 311px; width: 100%; height: 237px; background: var(--olive); color: var(--white); }
  .variety { left: 38px; top: 8px; font-weight: 600; font-size: 16px; }
  .uses { left: 38px; top: 35px; display: flex; gap: 9px; }
  .uses svg { width: 41px; height: 41px; }
  .shelf { left: 38px; top: 124px; font-weight: 600; font-size: 16px; line-height: 20px; }
  .storage { left: 38px; top: 182px; font-weight: 600; font-size: 16px; }
  .product { left: 331px; width: 400px; top: 4px; text-align: center; font-family: "Oranienbaum", serif; font-size: 80px; line-height: 90px; }
  .grade { left: 331px; width: 400px; top: 118px; text-align: center; font-family: "Montserrat", sans-serif; font-weight: 400; font-size: 32px; line-height: 46px; letter-spacing: 1px; }
  .nutrition { left: 813px; top: 26px; width: 212px; border: 1px solid var(--white); border-radius: 6px; overflow: hidden; font-weight: 300; font-size: 11px; }
  .nutrition__title { text-align: center; padding: 4px 0 3px; border-bottom: 1px solid var(--white); }
  .nutrition table { width: 100%; border-collapse: collapse; }
  .nutrition td { border-top: 1px solid var(--white); padding: 1px 0 1px 12px; height: 16.5px; }
  .nutrition tr:first-child td { border-top: none; }
  .nutrition td + td { border-left: 1px solid var(--white); text-align: center; padding-left: 0; width: 76px; }
  .volume { left: 825px; width: 200px; top: 184px; text-align: right; font-family: "Montserrat", sans-serif; font-weight: 700; font-size: 22px; }
</style>
</head>
<body>
<main class="label">
  <div class="leaf-decor leaf-decor--left" role="img" aria-label="Zarter Olivenzweig mit Blättern und Früchten"></div>
  <div class="leaf-decor leaf-decor--right" role="img" aria-label="Zarter Olivenzweig mit Blättern und Früchten"></div>

  <p class="abs facts">Sortenrein &amp; mühlenfrisch<br>Kaltgepresst<br>0,17% Ölsäure</p>

  <div class="abs donation">
    <svg class="donation__heart" viewBox="0 0 100 100" aria-hidden="true">
      <path d="M50 92 C20 66 4 50 4 30 C4 14 16 4 29 4 C39 4 46 10 50 18 C54 10 61 4 71 4 C84 4 96 14 96 30 C96 50 80 66 50 92Z" fill="var(--heart)"/>
    </svg>
    <p class="donation__text"><span>Wir Spenden</span><br>von Verkaufserlös</p>
  </div>

  <p class="abs est">Est. 2009</p>
  <div class="abs brand"><span class="brand__dot"></span><span class="brand__name">SEREVO</span></div>
  <p class="abs tagline">Kalt, elegant &amp; lecker</p>

  <div class="abs bottler">
    <p>Abgefüllt von Olivar Duro<br>für Serevo OHG<br>Am Lindenhof 12<br>22089 Hamburg<br>Deutschland</p>
    <p class="bottler__mail">info@serevo-oel.de</p>
  </div>

  <section class="band">
    <p class="abs variety">Sorte Arbequina, ideal zu:</p>
    <div class="abs uses">
      <svg viewBox="0 0 41 41" aria-label="Fisch" role="img">
        <rect x="1" y="1" width="39" height="39" rx="4" fill="none" stroke="#fff" stroke-width="2"/>
        <path d="M9 15 L14 20.5 L9 26 M14 20.5 C19 13 28 13 33 20.5 C28 28 19 28 14 20.5Z" fill="none" stroke="#fff" stroke-width="1.6"/>
        <circle cx="28" cy="19.5" r="1.2" fill="#fff"/>
      </svg>
      <svg viewBox="0 0 41 41" aria-label="Salat" role="img">
        <rect x="1" y="1" width="39" height="39" rx="4" fill="none" stroke="#fff" stroke-width="2"/>
        <path d="M9 22 H32 C32 29 27 33 20.5 33 C14 33 9 29 9 22Z M11 26 H30" fill="none" stroke="#fff" stroke-width="1.6"/>
        <circle cx="15" cy="17" r="3.5" fill="none" stroke="#fff" stroke-width="1.4"/>
        <circle cx="21" cy="13" r="3.5" fill="none" stroke="#fff" stroke-width="1.4"/>
        <circle cx="26" cy="18" r="3.5" fill="none" stroke="#fff" stroke-width="1.4"/>
      </svg>
      <svg viewBox="0 0 41 41" aria-label="Gebäck" role="img">
        <rect x="1" y="1" width="39" height="39" rx="4" fill="none" stroke="#fff" stroke-width="2"/>
        <path d="M8 24 C10 17 31 17 33 24 Z M9 24 L11 31 H30 L32 24" fill="none" stroke="#fff" stroke-width="1.6"/>
        <path d="M16 7 c-2 2 2 3 0 5 M20.5 7 c-2 2 2 3 0 5 M25 7 c-2 2 2 3 0 5" fill="none" stroke="#fff" stroke-width="1.3"/>
      </svg>
    </div>
    <p class="abs shelf">Mindestens haltbar bis:<br>Siehe Flasche</p>
    <p class="abs storage">Kühl und dunkel lagern</p>

    <h1 class="abs product" style="font-weight:400">Olivenöl</h1>
    <p class="abs grade">EXTRA NATIV<br>frühe Ernte</p>

    <div class="abs nutrition">
      <p class="nutrition__title">Durchschnittliche Nährwerte pro 100 g</p>
      <table>
        <tr><td></td><td>3700 kJ / 900 kJ</td></tr>
        <tr><td>Fett</td><td>100 g</td></tr>
        <tr><td>davon gesättigte Fettsäuren</td><td>100 g</td></tr>
        <tr><td>Kohlenhydrate</td><td>0,0 g</td></tr>
        <tr><td>davon Zucker</td><td>0,0 g</td></tr>
        <tr><td>Eiweiß</td><td>0,0 g</td></tr>
        <tr><td>Salz</td><td>0,0 g</td></tr>
      </table>
    </div>
    <p class="abs volume">250 ml</p>
  </section>
</main>
</body>
</html>
```